Business card design needed

Want the logo on a medium blue background and a nice funky design. I have my own gym and run one on one personal training and nutrition sessions. want it to look lively.
Updates

Please note I requested my logo on a blue background 

PLEASE NOTE: I already have a logo. It is attached to the order!!

Target Market(s)

over 55s

Industry/Entity Type

Nutrition

Contact Information for Business Card

Front of card : Logo ( on blue background )
Corinne Dalby
Nutrition & Fitness Coach for Seniors
Private gym at : 17 Fennick Street, Brantwood, Perth, WA 6291
Mob : 0412736158
Email : corinnedalby@fernpost.example
"For Seniors by a Senior"

Back of card
B.A. ( Soc.)
Dip. Ed. (Sec.)
Wellness Coach
Cert 4 Personal Trainer
Cert. Nutritition
MOVE ON Facilitator
Ageing Well Moving Freely Facilitator
NLP Master

```html
<!DOCTYPE html>
<html lang="en">
<head>
<meta charset="utf-8">
<title>Corinne Dalby Business Card</title>
<link rel="stylesheet" href="https://fonts.googleapis.com/css2?family=Ubuntu:wght@400;500;700&display=swap">
<style>
  :root {
    --stage: #e6e9ec;
    --brand-blue: #1f5e8d;
    --brand-blue-light: #5e9dc2;
    --brand-blue-deep: #174b73;
    --card-white: #ffffff;
    --card-white-shade: #eef0f2;
    --accent-yellow: #e6d21f;
    --ink: #2c2f33;
    --tab-light: #f4f5f6;
  }
  * { box-sizing: border-box; margin: 0; padding: 0; }
  html, body {
    width: 1200px;
    height: 861px;
    overflow: hidden;
  }
  body {
    background: var(--stage);
    font-family: "Ubuntu", sans-serif;
    position: relative;
  }
  .card {
    position: absolute;
    top: 255px;
    width: 545px;
    height: 345px;
    border-radius: 22px;
    overflow: hidden;
    box-shadow: 0 10px 28px rgba(0, 0, 0, 0.18);
    text-align: center;
  }
  .card--front {
    left: 35px;
    background: linear-gradient(200deg, var(--brand-blue-light) 0%, var(--brand-blue) 45%, var(--brand-blue-deep) 100%);
    color: var(--card-white);
  }
  .card--back {
    left: 620px;
    background: linear-gradient(160deg, var(--card-white) 0%, var(--card-white-shade) 100%);
    color: var(--brand-blue);
  }
  .slot {
    position: absolute;
    top: 112px;
    width: 34px;
    height: 130px;
    border-radius: 6px;
  }
  .slot--left { left: -6px; }
  .slot--right { right: -6px; }
  .card--front .slot { background: var(--tab-light); }
  .card--back .slot { background: var(--brand-blue); }

  .brand {
    margin-top: 46px;
    display: flex;
    align-items: center;
    justify-content: center;
    gap: 12px;
  }
  .brand__dot {
    width: 16px;
    height: 16px;
    border-radius: 50%;
  }
  .card--front .brand__dot { background: var(--card-white); }
  .card--back .brand__dot { background: var(--brand-blue); }
  .brand__name {
    font-size: 24px;
    font-weight: 500;
    line-height: 1.2;
  }
  .card--front .brand__name { color: var(--card-white); }
  .card--back .brand__name { color: var(--brand-blue); }

  .person__name {
    margin-top: 44px;
    font-size: 32px;
    font-weight: 700;
  }
  .person__role {
    margin-top: 4px;
    font-size: 18px;
  }
  .contact {
    margin-top: 22px;
    font-size: 15px;
    line-height: 1.6;
    list-style: none;
  }
  .contact__label { font-weight: 700; }

  .tagline {
    margin-top: 44px;
    font-size: 30px;
    font-weight: 700;
    color: var(--brand-blue);
  }
  .credentials {
    margin: 22px 0 0 100px;
    display: flex;
    gap: 16px;
    text-align: left;
    color: var(--ink);
  }
  .credentials__col {
    list-style: none;
    font-size: 15px;
    line-height: 1.65;
  }
  .credentials__col--narrow { font-size: 13.5px; line-height: 1.55; }
  .credentials__item {
    position: relative;
    padding-left: 16px;
  }
  .credentials__item::before {
    content: "";
    position: absolute;
    left: 0;
    top: 0.62em;
    width: 7px;
    height: 7px;
    border-radius: 50%;
    background: var(--accent-yellow);
  }
</style>
</head>
<body>
  <section class="card card--front" aria-label="Business card front">
    <span class="slot slot--left"></span>
    <span class="slot slot--right"></span>
    <div class="brand">
      <span class="brand__dot"></span>
      <span class="brand__name">Silver Stride Nutrition &amp; Fitness</span>
    </div>
    <h1 class="person__name">Corinne Dalby</h1>
    <p class="person__role">Nutrition &amp; Fitness Coach for Seniors</p>
    <ul class="contact">
      <li><span class="contact__label">Private gym:</span> 17 Fennick Street, Brantwood, Perth, WA 6291</li>
      <li><span class="contact__label">Mobile:</span> 0412736158</li>
      <li><span class="contact__label">Email:</span> corinnedalby@fernpost.example</li>
    </ul>
  </section>

  <section class="card card--back" aria-label="Business card back">
    <span class="slot slot--left"></span>
    <span class="slot slot--right"></span>
    <div class="brand">
      <span class="brand__dot"></span>
      <span class="brand__name">Silver Stride Nutrition &amp; Fitness</span>
    </div>
    <h2 class="tagline">For Seniors by a Senior</h2>
    <div class="credentials">
      <ul class="credentials__col">
        <li class="credentials__item">B.A. ( Soc.) Dip. Ed. (Sec.)</li>
        <li class="credentials__item">Wellness Coach</li>
        <li class="credentials__item">Certificate 4 Personal Trainer</li>
        <li class="credentials__item">Certificate Nutritition</li>
      </ul>
      <ul class="credentials__col credentials__col--narrow">
        <li class="credentials__item">MOVE ON Facilitator</li>
        <li class="credentials__item">Ageing Well Moving<br>Freely Facilitator</li>
        <li class="credentials__item">NLP Master</li>
      </ul>
    </div>
  </section>
</body>
</html>
```